KemaTruvi 16 pages booklet CD Cover

I need a cover (also formatted to be used for digital release), a 16 Pages Booklet + Inlay both sides, a back cover, and a CD image for french pop-rock album.

The name of the artist : Kematruvi
The name of the album : Cueillir la brume (which means "picking the mist")
Style of music: I've attached some mp3 extracts. In a few words, this is electro POP music, I'm inspired by band such as The Quill, etc..

This album talks about the desire to live elsewhere, in a world more just and equitable, less painful. The songs talk about people fighting to find a job, to feed their son, poeple who would like to have enough money to enjoy life, etc... but as they can't, at least, they dream about a new world, they draw this elsewhere, hence the title of the album "Cueillir la brume"

Industry/Entity Type

Music Download

Number of Pages Required

5+ page

Font styles to use
Sans Serif

Colors
b768aa
33a6d7

Requirements
Must have
• COver: fell free to make your porposal as long as it match the project description objectoves.
• I have add/attached a document "CD Cover Structure" that explains the stucture of the cover, and how i think it could be setup. BUt any other proposal will be welcome.
• For the last one, we will put the song titles and i will let you make me some suggestions.
Nice to have
• the songs are rather melancholy (but not sad) and it would be nice to transmit this impression by the colors. That's why i have chose the pink and blue as primary colours.

```html
<!DOCTYPE html>
<html lang="fr">
<head>
<meta charset="utf-8">
<title>Aux armes citoyens ! — Kematruvi</title>
<link href="https://fonts.googleapis.com/css2?family=Cutive+Mono&display=swap" rel="stylesheet">
<style>
  :root {
    --ink: #1c1a78;
    --paper: #ffffff;
    --magenta: #ee3fa8;
    --magenta-soft: #f590cf;
    --wash-cream: #fbf5d8;
    --wash-orange: #f6cf9a;
    --wash-blue: #c9d2f2;
    --wash-red: #e0606e;
  }
  html, body {
    margin: 0;
    padding: 0;
    overflow: hidden;
    background: var(--paper);
  }
  .booklet-page {
    position: relative;
    width: 1200px;
    height: 1200px;
    overflow: hidden;
    background:
      radial-gradient(ellipse 560px 520px at 560px 600px, var(--paper) 55%, rgba(255,255,255,0) 100%),
      radial-gradient(circle 260px at 0 0, var(--magenta) 20%, rgba(238,63,168,0) 100%),
      radial-gradient(circle 300px at 1200px 0, var(--magenta) 25%, rgba(238,63,168,0) 100%),
      radial-gradient(circle 320px at 0 1200px, var(--magenta) 25%, rgba(238,63,168,0) 100%),
      radial-gradient(circle 200px at 1200px 1200px, var(--magenta-soft) 10%, rgba(245,144,207,0) 100%),
      radial-gradient(ellipse 420px 140px at 600px 0, var(--magenta) 10%, rgba(238,63,168,0) 100%),
      radial-gradient(ellipse 140px 420px at 0 600px, var(--magenta) 15%, rgba(238,63,168,0) 100%),
      radial-gradient(ellipse 160px 380px at 1200px 420px, var(--magenta) 15%, rgba(238,63,168,0) 100%),
      var(--paper);
    font-family: "Cutive Mono", "Courier New", monospace;
    color: var(--ink);
  }
  .song-header {
    position: absolute;
    left: 76px;
    top: 160px;
    margin: 0;
    font-weight: 400;
    font-size: 24px;
    line-height: 41px;
    letter-spacing: 3.3px;
  }
  .song-header span { display: block; }
  .lyrics {
    position: absolute;
    left: 76px;
    top: 310px;
    margin: 0;
    font-size: 14px;
    line-height: 23.6px;
    letter-spacing: 1.4px;
    white-space: pre;
  }
  .lyrics p { margin: 0 0 23.6px 0; }
  .artwork-dream {
    position: absolute;
    left: 745px;
    top: 495px;
    width: 385px;
    height: 430px;
    border-radius: 46% 50% 44% 48%;
    background: radial-gradient(ellipse at 45% 45%, var(--wash-cream) 25%, var(--wash-orange) 55%, rgba(246,207,154,0.15) 80%);
  }
  .artwork-crowd {
    position: absolute;
    left: 565px;
    top: 1030px;
    width: 400px;
    height: 170px;
    background: linear-gradient(90deg, var(--wash-blue) 0%, #e8ecfb 45%, var(--wash-red) 70%, #e8ecfb 100%);
    border-radius: 40px 40px 0 0;
    opacity: 0.75;
  }
</style>
</head>
<body>
  <main class="booklet-page">
    <h1 class="song-header">
      <span class="song-title">Aux armes citoyens !</span>
      <span class="song-dedication">(aux Indignés, aux sans-dents et aux fainéants)</span>
      <span class="song-author">(Paul Mirande-Kematruvi)</span>
    </h1>

    <div class="lyrics">
<p>C C G G Am Am F F
Combien de temps allons-nous attendre
Avant de comprendre et de prendre conscience
Qu’il ne sert à rien de compter sur lui
Mes Frères et sœurs allons-y
Si le monde meilleur reste à construire
Il commence ici avec un doux sourire
Ne laissons plus la peur répondre à nos erreurs
On ne doit pas nous dire ce qu’est le bonheur
Deux mille ans nous regardent Divinités malades
L’injustice et la foi sous des croissants et des croix
Il est temps, Il est temps de rêver en cadence
Ne laissons plus la terre aux mains de ces mercenaires
Ne donnons pas nos vies, nous avons bien trop subi,
Nous avons bien trop subi.</p>
<p>Allez, allez, sommes-nous vraiment ces gentils moutons
Comme ils nous voudraient à survivre comme des cons
Ne laissons plus les autres décider pour nous
Ni les dieux qui nous mettent à genoux
Ni les seigneurs qui veulent confisquer la lumière
Soyons libres et rêvons jusqu’au bout pour la terre
Soyons libres et changeons ce destin qui nous tient
Et cessons d’attendre… Oui cessons d’attendre, oui cessons d’attendre…
Nos armes ne seront plus à vendre
Aux armes citoyens !</p>
<p>Nosotros somos los Indignados, les fils de Varnel,
les fils de Varnel, de Lucien Varnel</p>
    </div>

    <div class="artwork-dream" role="img" aria-label="Sketched thought bubble showing a sheep lounging in an armchair with a bottle and a remote control"></div>
    <div class="artwork-crowd" role="img" aria-label="Sketched crowd of people seen from behind, dreaming the scene above"></div>
  </main>
</body>
</html>
```